Coral Beacon Stationery Design Project

I am looking for a suitable stationary design for my company Coral Beacon Pty Ltd (ACN 582 914 306).

The requirements can be better explained by visiting my website
"coral-beacon-trust.org"

I will be sending letters to Ministers of State and the Heads of Government Agencies so the theme needs to be formal and serious.

A theme with a shield or similar picking on the "guardian" concept would be appropriate

Target Market(s)

Ministers of State and Department Agency Heads and legal firms, the heads of Trustee Companies as well as Members of Coral Beacon

Industry/Entity Type

Government

Requirements
Must have
• Letterhead design is a priority - Business Card secondary

Must include tag line "Steady hands for every estate we tend" with a registered trade mark superscript at the end that is an R in a circle {Windows Alt +0174 on numeric keypad or Mac Option +R}.

Must include website address "Coral-Beacon-Trust.org" plus Email address "corbeacon@mailvessel.net

Company name "Coral Beacon Pty. Ltd." and Australian Company Number "ACN 582 914 306" needs to be shown more discretely

Address is "47 Finch Crescent, Marrowdale, 3291"
Nice to have
• A watermark is something to be considered

```html
<!DOCTYPE html>
<html lang="en">
<head>
<meta charset="utf-8">
<title>Coral Beacon Business Card</title>
<link href="https://fonts.googleapis.com/css2?family=Barlow:wght@400;500;600&display=swap" rel="stylesheet">
<style>
  :root {
    --stage: #9d9d9d;
    --card-light: #f1f1f1;
    --card-light-edge: #dcdcdc;
    --card-dark: #050505;
    --ink: #111111;
    --gold: #c9a35a;
    --gold-deep: #a8843e;
    --white: #ffffff;
  }
  * { margin: 0; padding: 0; box-sizing: border-box; }
  html, body {
    width: 1200px;
    height: 720px;
    overflow: hidden;
    background: var(--stage);
    font-family: "Barlow", Arial, sans-serif;
  }
  .stage {
    width: 1200px;
    height: 720px;
    display: flex;
    align-items: center;
    justify-content: center;
    gap: 60px;
  }
  .card {
    position: relative;
    width: 520px;
    height: 318px;
    box-shadow: 0 10px 24px rgba(0,0,0,0.28);
  }
  .card--front {
    background: linear-gradient(135deg, var(--card-light) 0%, var(--card-light-edge) 100%);
    color: var(--ink);
  }
  .card--back {
    background: var(--card-dark);
    color: var(--white);
  }
  .brand {
    position: absolute;
    left: 32px;
    top: 30px;
  }
  .brand__row {
    display: flex;
    align-items: center;
    gap: 12px;
  }
  .brand__mark {
    width: 40px;
    height: 40px;
    background: var(--gold);
  }
  .brand__name {
    font-size: 30px;
    font-weight: 600;
    letter-spacing: 0.5px;
    line-height: 1;
  }
  .card--front .brand__name { color: var(--ink); }
  .card--back .brand__name { color: var(--white); }
  .brand__tagline {
    margin: 6px 0 0 52px;
    font-size: 11.5px;
    font-weight: 500;
    color: var(--gold);
    letter-spacing: 0.3px;
  }
  .brand__tagline sup { font-size: 8px; }
  .person {
    position: absolute;
    left: 32px;
    top: 118px;
  }
  .person__name {
    font-size: 20px;
    font-weight: 500;
    color: var(--gold);
    line-height: 1.1;
  }
  .person__role {
    font-size: 14px;
    font-weight: 500;
    color: var(--ink);
  }
  .contact {
    position: absolute;
    left: 32px;
    top: 182px;
    font-size: 16px;
    font-weight: 500;
    line-height: 1.28;
    font-style: normal;
  }
  .contact__address { color: var(--gold); }
  .contact__label { color: var(--ink); }
  .contact__value { color: var(--gold); }
  .website {
    position: absolute;
    right: 30px;
    bottom: 28px;
    font-size: 18px;
    font-weight: 500;
    color: var(--gold);
    letter-spacing: 0.3px;
  }
</style>
</head>
<body>
<main class="stage">
  <section class="card card--front" aria-label="Business card front">
    <div class="brand">
      <div class="brand__row">
        <span class="brand__mark"></span>
        <span class="brand__name">Coral Beacon</span>
      </div>
      <p class="brand__tagline">Steady hands for every estate we tend<sup>®</sup></p>
    </div>
    <div class="person">
      <p class="person__name">Daniel Hartwell</p>
      <p class="person__role">Director</p>
    </div>
    <address class="contact">
      <div class="contact__address">47 Finch Crescent,<br>Marrowdale, 3291</div>
      <div><span class="contact__label">Phone:</span> <span class="contact__value">0438 205 917</span></div>
      <div><span class="contact__label">Fax:</span> <span class="contact__value">(02) 9471 3068</span></div>
      <div><span class="contact__label">Email:</span> <span class="contact__value">corbeacon@mailvessel.net</span></div>
    </address>
  </section>

  <section class="card card--back" aria-label="Business card back">
    <div class="brand">
      <div class="brand__row">
        <span class="brand__mark"></span>
        <span class="brand__name">Coral Beacon</span>
      </div>
      <p class="brand__tagline">Steady hands for every estate we tend<sup>®</sup></p>
    </div>
    <p class="website">www.Coral-Beacon-Trust.org</p>
  </section>
</main>
</body>
</html>
```